The Harvest Compass

Cutting Through the Noise to What Actually Works.

Nutrition book

Target Market(s)

People looking to be or get healthy and eat right.

```html
<!DOCTYPE html>
<html lang="en">
<head>
<meta charset="utf-8">
<title>The Harvest Compass — Book Cover</title>
<link href="https://fonts.googleapis.com/css2?family=League+Spartan:wght@800;900&family=Montserrat:wght@500&display=swap" rel="stylesheet">
<style>
  :root {
    --backdrop: #bfc0c2;
    --cover-top: #98b064;
    --cover-mid: #86a25a;
    --cover-deep: #557a35;
    --cover-bottom: #486529;
    --title-dark: #17100c;
    --title-red: #c9232b;
    --author: #ffffff;
    --tier-fats: #e9a838;
    --tier-protein: #d9542e;
    --tier-produce: #6f9a3f;
    --tier-meals: #3d8cc4;
  }
  * { margin: 0; padding: 0; box-sizing: border-box; }
  html, body {
    width: 1200px;
    height: 1200px;
    overflow: hidden;
    background: var(--backdrop);
  }
  .canvas {
    position: relative;
    width: 1200px;
    height: 1200px;
  }
  .book-cover {
    position: absolute;
    left: 360px;
    top: 240px;
    width: 480px;
    height: 720px;
    background: linear-gradient(180deg,
      var(--cover-top) 0%,
      var(--cover-top) 32%,
      var(--cover-mid) 50%,
      var(--cover-deep) 68%,
      var(--cover-bottom) 100%);
    overflow: hidden;
  }
  .title {
    position: absolute;
    left: 0;
    width: 100%;
    text-align: center;
    font-family: "League Spartan", "Arial Black", sans-serif;
    font-weight: 900;
    text-transform: uppercase;
    line-height: 1;
    letter-spacing: 0.5px;
    white-space: nowrap;
  }
  .title-the { top: 58px; font-size: 66px; color: var(--title-dark); }
  .title-harvest { top: 128px; font-size: 78px; color: var(--title-red); }
  .title-compass { top: 198px; font-size: 78px; color: var(--title-dark); }
  .food-pyramid {
    position: absolute;
    left: 0;
    top: 0;
    width: 480px;
    height: 720px;
  }
  .author-name {
    position: absolute;
    left: 0;
    width: 100%;
    top: 648px;
    text-align: center;
    font-family: "Montserrat", "Helvetica", sans-serif;
    font-weight: 500;
    font-size: 27px;
    letter-spacing: 4.5px;
    color: var(--author);
    text-transform: uppercase;
  }
</style>
</head>
<body>
<main class="canvas">
  <section class="book-cover">
    <h1 class="title-block">
      <span class="title title-the">The</span>
      <span class="title title-harvest">Harvest</span>
      <span class="title title-compass">Compass</span>
    </h1>

    <svg class="food-pyramid" viewBox="0 0 480 720" xmlns="http://www.w3.org/2000/svg">
      <polygon role="img" aria-label="Healthy fats: olive oil, avocado, nuts and dark chocolate"
        points="240,302 292,399 188,399" fill="var(--tier-fats)"/>
      <polygon role="img" aria-label="Proteins: salmon, chicken, steak, eggs and yogurt"
        points="186,402 294,402 334.5,477 145.5,477" fill="var(--tier-protein)"/>
      <polygon role="img" aria-label="Vegetables, fruits, whole grains and nuts"
        points="144,480 336,480 377,555 103,555" fill="var(--tier-produce)"/>
      <polygon role="img" aria-label="Balanced meal bowls beside a wall clock"
        points="102,558 378,558 411,619 69,619" fill="var(--tier-meals)"/>
    </svg>

    <p class="author-name">Author Name</p>
  </section>
</main>
</body>
</html>
```